MARLO Real Estate Prospecting DL Flyer

I need a DL size (99mm x 210mm) two sided flyer designed for letter boxing and also handing to prospective clients when door knocking across my sales area in Melbourne, Australia. PLEASE NOTE: the flyer is a flat flyer to be designed on both sides as per my doc below. The flyer will likely be printed on 350gsm card. It will not be posted - so NO space for address required. It is for door-knocking (door to door sales) and letter boxing (dropped personally by me in a letterbox - not posted).
My original company logo design brief was that it should be modern and premium black on white and white on black - drawing influences by FELIX DORNE and also CALISTA. I want my DL flyer to reflect the same influence. I have attached proposed copy on the word document attached below.
The DL flyer will be printed on 350 gsm - probably gloss to reflect the premium feel, but open to suggestion. It is important for the flyer to be durable and have decent shelf life - I am not going for cheap and cheerful on this project. I need to make an impact. I am trying to attract home owners to my business to list and sell their properties - usually for most people their biggest asset is their home/property - so it is important that my business is credible and very experienced (which of course it is).
For a view of the types of properties I sell please go to www.homelistingsdemo.com.au and type in Mount Waverley, Victoria; and also Glen Waverley, Victoria. You will see a list of properties come up that are either for SALE or for SALE BY AUCTION. This may help with your understanding. The areas I concentrate on are very suburban - meaning families, families, families :)

Target Market(s)

Property owners across the middle ring of eastern suburbs of Melbourne. Value of homes are between $1m and $2m, and mostly consist of 3 and 4 bedroom family homes. Clients range from the elderly looking to downsize to a smaller property, to families looking to sell and upgrade their homes.

Industry/Entity Type

Real Estate Agent

Font styles to use
Serif

Colors
000000
ffffff

Requirements
Must have
• The "call to action" components that I have included on the doc file and include a FREE E-BOOK on supply of their contact details; and a FREE PROFESSIONAL HOME STYLIST CONSULTATION.
• It must feature my company logo. My corporate colours are black and white - so best to stick with these in the design.
• UPDATE: Just call the e-book "5 EASY STEPS TO LIFT THE FINAL OFFER ON YOUR HOUSE"
• ...forget the City of Brellton and City of Parkvane part!!
• UPDATE: Designs I have liked the best include the following elements:
• 1. Strong brand at top of each side of flyer
• 2. Family pic page 1; property pic page 2
• 3. BOLD Headings
• 4. Amplified CALL TO ACTION - FREE......consult; FREE E-Book
• 5. Clear visible contact details at bottom of page
Nice to have
• Lifestyle photography of homes.
• Some designers have used Asian families in their pics - which is smart as the main buyer demographic is Chinese families. The mail ownership is Australian - so a mix of Asian and Anglo is fine. Try and avoid overtly USA style properties - as Melbourne styles are different. Keys, handshakes etc are all good :)
Should not have
• Animation, cartoons, or visual drawings included.

```html
<!DOCTYPE html>
<html lang="en">
<head>
<meta charset="utf-8">
<title>MARLO Real Estate – DL Flyer</title>
<link href="https://fonts.googleapis.com/css2?family=Montserrat:wght@400;500;600;700;800&family=Bebas+Neue&family=Open+Sans:ital,wght@1,600&display=swap" rel="stylesheet">
<style>
:root{
  --ink:#111;
  --panel:#1e1e1e;
  --paper:#fff;
  --text-light:#e8e8e8;
  --stage:#d6d6d6;
}
*{margin:0;padding:0;box-sizing:border-box}
html,body{width:1200px;height:1200px;overflow:hidden}
body{background:var(--stage);font-family:"Montserrat",sans-serif;position:relative}
.flyer{position:absolute;top:84px;width:495px;height:1048px;overflow:hidden;background:var(--panel);box-shadow:0 4px 14px rgba(0,0,0,.25)}
.flyer--front{left:87px}
.flyer--back{left:612px;background:linear-gradient(180deg,#1a1a1a 0%,#2a2a2a 55%,#222 100%)}
.layer{position:absolute;left:0;width:100%}
.brand{position:absolute;top:26px;left:0;width:100%;text-align:center;z-index:3}
.brand__name{font-weight:700;font-size:96px;line-height:82px;letter-spacing:2px}
.brand__sub{font-weight:400;font-size:16px;letter-spacing:17.5px;margin-top:16px;padding-left:17px}
.flyer--front .brand{color:var(--ink)}
.flyer--back .brand{color:var(--paper)}
.photo{top:150px;height:270px;background:linear-gradient(160deg,#f2f2f2 0%,#dcdcdc 45%,#c9b8a8 70%,#ececec 100%)}
.headline{position:absolute;left:0;width:100%;text-align:center;font-weight:800;font-size:27px;line-height:31px;color:#d9d9d9;text-shadow:0 2px 2px #000;z-index:3}
.pill{position:absolute;left:50px;top:518px;width:395px;height:60px;border-radius:30px;background:linear-gradient(180deg,#fafafa,#bdbdbd 55%,#e0e0e0);border:2px solid #777;display:flex;align-items:center;justify-content:center;text-align:center;font-family:"Open Sans",sans-serif;font-style:italic;font-weight:600;font-size:15.5px;line-height:21px;color:#1a1a1a;z-index:3}
.body-copy{position:absolute;left:25px;right:25px;color:var(--text-light);font-size:11.4px;line-height:17.6px;text-align:justify;z-index:3}
.body-copy b{font-weight:700;color:#fff}
.ticks{position:absolute;left:25px;right:25px;top:683px;list-style:none;color:var(--text-light);font-size:11.4px;line-height:15px;z-index:3}
.ticks li{display:flex;gap:10px;margin-bottom:10px}
.ticks svg{flex:none;margin-top:1px}
.ebook-title{position:absolute;top:794px;left:0;width:100%;text-align:center;font-family:"Bebas Neue",sans-serif;font-size:40px;color:#dcdcdc;text-shadow:0 2px 2px #000;z-index:3}
.offer-box{position:absolute;left:25px;right:25px;border:1px solid #6d6d6d;z-index:2}
.offer-box--front{top:855px;height:110px}
.offer-box--back{top:806px;height:160px}
.quote-mark{position:absolute;left:50%;top:-16px;margin-left:-16px;width:32px;height:32px;border-radius:50%;border:2px solid #bbb;background:var(--panel);color:#ddd;font:800 24px/34px "Montserrat",sans-serif;text-align:center}
.offer-text{position:absolute;left:0;width:100%;text-align:center;color:#eee;font-weight:600;z-index:3}
.offer-text--front{top:875px;font-size:12.4px;line-height:16.5px}
.offer-text--back{top:832px;font-size:16.8px;line-height:20.5px;padding:0 30px}
.footer-curve{bottom:0;height:160px;z-index:2}
.contact{position:absolute;left:0;width:100%;bottom:0;height:110px;text-align:center;z-index:4;color:var(--ink)}
.contact__lead{font-family:"Bebas Neue",sans-serif;font-size:25px;line-height:26px;margin-top:9px}
.contact__phone{font-weight:800;font-size:40px;line-height:42px;display:flex;justify-content:center;align-items:center;gap:6px}
.contact__email{font-size:18px;line-height:22px;display:flex;justify-content:center;align-items:center;gap:14px}
.portrait{position:absolute;left:84px;top:428px;width:316px;height:378px;background:radial-gradient(ellipse at 50% 40%,#4a4a4a 0%,#2a2a2a 60%,transparent 75%);z-index:1}
</style>
</head>
<body>

<section class="flyer flyer--front">
  <div class="layer photo" role="img" aria-label="Photo of an open hand holding house keys beside a hand holding a small model house"></div>
  <svg class="layer" style="top:0;height:240px;z-index:1" width="495" height="240" viewBox="0 0 495 240"><path d="M0 0 H495 V132 Q300 290 0 214 Z" fill="#efefef"/></svg>
  <div class="brand"><div class="brand__name">MARLO</div><div class="brand__sub">REAL ESTATE</div></div>

  <svg class="layer" style="top:0;height:1048px;z-index:2" width="495" height="1048" viewBox="0 0 495 1048">
    <defs>
      <linearGradient id="silverA" x1="0" x2="1"><stop offset="0" stop-color="#777"/><stop offset=".5" stop-color="#f2f2f2"/><stop offset="1" stop-color="#9a9a9a"/></linearGradient>
    </defs>
    <path d="M0 214 Q300 290 495 132 L495 152 Q300 300 0 220 Z" fill="#222"/>
    <path d="M0 412 Q 250 340 495 400 L495 1048 L0 1048 Z" fill="#1e1e1e"/>
    <path d="M0 412 Q 250 340 495 400 L495 420 Q 250 362 0 440 Z" fill="url(#silverA)"/>
  </svg>

  <h2 class="headline" style="top:444px">GET THE MAXIMUM PRICE<br>FOR YOUR PROPERTY</h2>
  <div class="pill">Personal Service, Clear Communication, Honest<br>Advice, Top Results, For A SetFee™</div>
  <p class="body-copy" style="top:596px">At MARLO Real Estate we are doing things differently. Our property sales process is designed to extract an ELITE LEVEL PRICE for you, but our cost of doing business is significantly reduced from that of our competitors, and that results in MORE MONEY IN YOUR POCKET.</p>
  <ul class="ticks">
    <li><svg width="14" height="14" viewBox="0 0 14 14"><circle cx="7" cy="7" r="7" fill="#bbb"/><path d="M4 7.2l2 2 4-4.2" stroke="#222" stroke-width="1.6" fill="none"/></svg><span>ELITE sales process ensures the maximum possible price for your property.</span></li>
    <li><svg width="14" height="14" viewBox="0 0 14 14"><circle cx="7" cy="7" r="7" fill="#bbb"/><path d="M4 7.2l2 2 4-4.2" stroke="#222" stroke-width="1.6" fill="none"/></svg><span>Low SETFEE™ selling commission – up to half that charged by other agents.</span></li>
    <li><svg width="14" height="14" viewBox="0 0 14 14"><circle cx="7" cy="7" r="7" fill="#bbb"/><path d="M4 7.2l2 2 4-4.2" stroke="#222" stroke-width="1.6" fill="none"/></svg><span>A SETFEE™ in high impact marketing for the sale of your home.</span></li>
  </ul>
  <h3 class="ebook-title">GET YOUR FREE COPY OF MY E-BOOK</h3>
  <div class="offer-box offer-box--front"><div class="quote-mark">“</div></div>
  <p class="offer-text offer-text--front">5 EASY STEPS TO LIFT THE FINAL OFFER ON YOUR HOUSE<br>IN THE CITY OF BRELLTON AND THE CITY OF PARKVANE</p>

  <svg class="layer footer-curve" width="495" height="160" viewBox="0 0 495 160">
    <defs><linearGradient id="silverB" x1="0" x2="1"><stop offset="0" stop-color="#8a8a8a"/><stop offset=".5" stop-color="#e6e6e6"/><stop offset="1" stop-color="#8a8a8a"/></linearGradient></defs>
    <path d="M0 66 Q 248 -26 495 66 V160 H0 Z" fill="url(#silverB)"/>
    <path d="M0 100 Q 248 -20 495 100 V160 H0 Z" fill="#fff"/>
  </svg>
  <div class="contact">
    <div class="contact__lead">JUST CALL OR EMAIL</div>
    <div class="contact__phone"><svg width="30" height="30" viewBox="0 0 24 24"><path d="M6.6 3.5l2.6 3.4-1.6 2c1 2.4 3 4.4 5.4 5.4l2-1.6 3.4 2.6-1.6 2.6c-6.4-.4-11.8-5.8-12.2-12.2z" fill="#111"/><path d="M14 4a6 6 0 016 6M14 7a3 3 0 013 3" stroke="#111" stroke-width="1.6" fill="none"/></svg>1800 555 019</div>
    <div class="contact__email"><svg width="20" height="14" viewBox="0 0 20 14"><rect x="1" y="1" width="18" height="12" fill="none" stroke="#111" stroke-width="1.6"/><path d="M1 1l9 7 9-7" stroke="#111" stroke-width="1.6" fill="none"/></svg>sales@marlorealestate.com.au</div>
  </div>
</section>

<section class="flyer flyer--back">
  <div class="brand"><div class="brand__name">MARLO</div><div class="brand__sub">REAL ESTATE</div></div>
  <svg class="layer" style="top:150px;height:70px;z-index:2" width="495" height="70" viewBox="0 0 495 70">
    <defs><linearGradient id="silverC" x1="0" x2="1"><stop offset="0" stop-color="#666"/><stop offset=".5" stop-color="#f0f0f0"/><stop offset="1" stop-color="#777"/></linearGradient></defs>
    <path d="M0 60 Q 250 -10 495 45 Q 250 10 0 70 Z" fill="url(#silverC)"/>
  </svg>
  <h2 class="headline" style="top:218px">A DECADE OF EXPERIENCE<br>ON YOUR SIDE</h2>
  <p class="body-copy" style="top:294px"><b>My name's Daniel Marlo.</b> With over a decade of experience in the property industry I know what it takes to get you the BEST POSSIBLE PRICE for your property. I've spent much of my career in the cutthroat world of commercial property and closing high stakes international real estate deals. But 3 years ago I brought my expertise home to focus on the communities in Melbourne's eastern suburbs. I've had many incredible sales results to date. Will yours be next?</p>
  <div class="portrait" role="img" aria-label="Portrait of the agent in a dark suit, white shirt and striped tie"></div>
  <div class="offer-box offer-box--back"></div>
  <p class="offer-text offer-text--back">Claim Your Free Property Market Appraisal Now And Receive A BONUS Professional Home Stylist Consultation – Normally Worth $118</p>

  <svg class="layer footer-curve" width="495" height="160" viewBox="0 0 495 160">
    <defs><linearGradient id="silverD" x1="0" x2="1"><stop offset="0" stop-color="#8a8a8a"/><stop offset=".5" stop-color="#e6e6e6"/><stop offset="1" stop-color="#8a8a8a"/></linearGradient></defs>
    <path d="M0 66 Q 248 -26 495 66 V160 H0 Z" fill="url(#silverD)"/>
    <path d="M0 100 Q 248 -20 495 100 V160 H0 Z" fill="#fff"/>
  </svg>
  <div class="contact">
    <div class="contact__lead">JUST CALL OR EMAIL</div>
    <div class="contact__phone"><svg width="30" height="30" viewBox="0 0 24 24"><path d="M6.6 3.5l2.6 3.4-1.6 2c1 2.4 3 4.4 5.4 5.4l2-1.6 3.4 2.6-1.6 2.6c-6.4-.4-11.8-5.8-12.2-12.2z" fill="#111"/><path d="M14 4a6 6 0 016 6M14 7a3 3 0 013 3" stroke="#111" stroke-width="1.6" fill="none"/></svg>1800 555 019</div>
    <div class="contact__email"><svg width="20" height="14" viewBox="0 0 20 14"><rect x="1" y="1" width="18" height="12" fill="none" stroke="#111" stroke-width="1.6"/><path d="M1 1l9 7 9-7" stroke="#111" stroke-width="1.6" fill="none"/></svg>sales@marlorealestate.com.au</div>
  </div>
</section>

</body>
</html>
```